Online Art Gallery & Art Management Firm looking for a business card

I'm launching an online art gallery (paintings, photography, drawings, furniture, books, ...) where people can buy all types of art. It's a platform where young and unknown artists can showcase their oeuvre.

Additionally, the venture will act as my advising company for artists. I help them out with their business side of life and become their representative.

The company name: The Velvet Parlour
Logo is attached

I'm looking for something very classy and upmarket.
Updates

Reason: Logo wasn't finished yet...

The design should include the following information: - Name: Pieter Vandomme - Title: Founder - Mobile: +32 (0) 486 514 362 - E-mail: pieter@velvet-parlour.example - Website www.velvet-parlour.example I prefer the have the logo (without website) on the one side and the information on the other. Best regards Pieter

Target Market(s)

Art buyers / art dealers / artists / middle class / upmarket /

Industry/Entity Type

Artists

Colors

Designer to choose colors to be used in the design.

Requirements
Must have
• Must communicate credibility, trust and integrity
Nice to have
• Something classy, chique
Should not have
• Nothing to artistic or creative

```html
<!DOCTYPE html>
<html lang="en">
<head>
<meta charset="utf-8">
<title>The Velvet Parlour — Business Card</title>
<link rel="stylesheet" href="https://fonts.googleapis.com/css2?family=Cinzel:wght@400&family=Crimson+Text:wght@400&display=swap">
<style>
  :root {
    --backdrop: #2b2533;
    --card-light: #ffffff;
    --card-dark: #050505;
    --ink: #111111;
    --ink-inverse: #f2f2f2;
    --rule: #111111;
  }
  * { box-sizing: border-box; margin: 0; padding: 0; }
  html, body {
    width: 1200px;
    height: 1000px;
    overflow: hidden;
    background: var(--backdrop);
  }
  .sheet {
    width: 1200px;
    height: 1000px;
    display: flex;
    flex-direction: column;
    align-items: center;
    justify-content: center;
    gap: 56px;
  }
  .card {
    position: relative;
    width: 680px;
    height: 420px;
    box-shadow: 0 10px 30px rgba(0, 0, 0, 0.35);
  }
  .card--front { background: var(--card-light); color: var(--ink); }
  .card--back {
    background: var(--card-dark);
    color: var(--ink-inverse);
    display: flex;
    align-items: center;
    justify-content: center;
  }
  .wordmark {
    font-family: "Cinzel", serif;
    font-weight: 400;
    text-transform: uppercase;
    letter-spacing: 0.32em;
    white-space: nowrap;
  }
  .card--front .wordmark {
    position: absolute;
    top: 42px;
    right: 40px;
    font-size: 30px;
  }
  .card--back .wordmark { font-size: 40px; letter-spacing: 0.28em; }
  .person {
    position: absolute;
    top: 112px;
    left: 70px;
    text-align: center;
  }
  .person__name {
    font-family: "Cinzel", serif;
    font-weight: 400;
    font-size: 28px;
    letter-spacing: 0.02em;
  }
  .person__title {
    font-family: "Crimson Text", serif;
    font-size: 24px;
    margin-top: 2px;
  }
  .contact {
    position: absolute;
    right: 56px;
    bottom: 42px;
    width: 300px;
    font-family: "Crimson Text", serif;
    font-size: 19px;
    line-height: 1.2;
    text-align: right;
  }
  .contact__rule {
    display: block;
    height: 2px;
    background: var(--rule);
    width: 150px;
  }
  .contact__rule--top { margin: 0 0 10px auto; }
  .contact__rule--bottom { margin: 10px auto 0 0; width: 170px; margin-left: 40px; }
  .contact__line { display: block; }
</style>
</head>
<body>
  <main class="sheet">
    <section class="card card--front" aria-label="Card front with contact details">
      <h1 class="wordmark">The Velvet Parlour</h1>
      <div class="person">
        <p class="person__name">Pieter Vandomme</p>
        <p class="person__title">Founder</p>
      </div>
      <address class="contact" style="font-style: normal;">
        <span class="contact__rule contact__rule--top"></span>
        <span class="contact__line">+32 (0) 486 514 362</span>
        <span class="contact__line">pieter@velvet-parlour.example</span>
        <span class="contact__line">www.velvet-parlour.example</span>
        <span class="contact__rule contact__rule--bottom"></span>
      </address>
    </section>
    <section class="card card--back" aria-label="Card back with name">
      <p class="wordmark">The Velvet Parlour</p>
    </section>
  </main>
</body>
</html>
```